Business Card Design Project

My business sells promotional merchandise to large blue chip companies. Gear like polo shirts, drink bottles, pens, basically anything that you can put a company logo onto.

I need the following elements included:
Logo as attached
Peter Hallorand Managing Director
21 Kestrel Court Thornlea 4168
mobile 0438 612054
email tidewell@tidewellcoastal.com.au

Promotional Merchandise with a difference

Mature age Marketing Managers

Business

```html
<!DOCTYPE html>
<html lang="en">
<head>
<meta charset="UTF-8">
<title>Tidewell Business Card</title>
<link rel="stylesheet" href="https://fonts.googleapis.com/css2?family=Crimson+Text:wght@400&family=Source+Sans+3:wght@400;600&display=swap">
<style>
  :root {
    --page-bg: #ffffff;
    --navy: #283a78;
    --card-light: #f2efe6;
    --card-mid: #e4e0d1;
    --card-edge: #d3ceba;
    --ink: #1c1c1c;
    --white: #ffffff;
  }
  * { margin: 0; padding: 0; box-sizing: border-box; }
  html, body {
    width: 1200px;
    height: 900px;
    overflow: hidden;
    background: var(--page-bg);
  }
  .canvas {
    position: relative;
    width: 1200px;
    height: 900px;
  }
  .card {
    position: absolute;
    left: 386px;
    top: 72px;
    width: 428px;
    height: 754px;
    background: radial-gradient(ellipse 70% 55% at 50% 42%, var(--card-light) 0%, var(--card-mid) 65%, var(--card-edge) 100%);
    overflow: hidden;
  }
  .card__top-band {
    position: absolute;
    left: 0; top: 0;
    width: 100%;
    height: 38px;
    background: var(--navy);
  }
  .brand {
    position: absolute;
    left: 66px;
    top: 140px;
    width: 296px;
    height: 106px;
    background: var(--white);
    display: flex;
    align-items: center;
    justify-content: center;
  }
  .brand__name {
    font-family: "Source Sans 3", sans-serif;
    font-weight: 600;
    font-size: 48px;
    letter-spacing: 1px;
    color: var(--navy);
    line-height: 1;
  }
  .person {
    position: absolute;
    right: 16px;
    top: 474px;
    text-align: right;
    font-family: "Crimson Text", serif;
    color: var(--ink);
  }
  .person__name {
    font-size: 31px;
    line-height: 38px;
  }
  .person__title {
    font-size: 18px;
    line-height: 22px;
  }
  .contact {
    position: absolute;
    left: 14px;
    top: 620px;
    font-family: "Crimson Text", serif;
    font-size: 18px;
    line-height: 22px;
    color: var(--ink);
    list-style: none;
  }
  .card__tagline {
    position: absolute;
    left: 0; bottom: 0;
    width: 100%;
    height: 36px;
    background: var(--navy);
    color: var(--white);
    font-family: "Source Sans 3", sans-serif;
    font-weight: 400;
    font-size: 20px;
    line-height: 36px;
    text-align: center;
  }
</style>
</head>
<body>
<main class="canvas">
  <article class="card">
    <div class="card__top-band"></div>

    <div class="brand">
      <span class="brand__name">TIDEWELL</span>
    </div>

    <div class="person">
      <p class="person__name">Peter Hallorand</p>
      <p class="person__title">Managing Director</p>
    </div>

    <ul class="contact">
      <li class="contact__address">21 Kestrel Court Thornlea 4168</li>
      <li class="contact__mobile">mobile : 0438 612054</li>
      <li class="contact__email">email : tidewell@tidewellcoastal.com.au</li>
    </ul>

    <p class="card__tagline">Promotional Merchandise with a difference</p>
  </article>
</main>
</body>
</html>
```